Upcoming Guitar Teacher needs a Rock Star PDF of online course

We are in the process of revising our online course and need to make more visually appealing PDFs for students. We help regular folks learn how to play their favorite songs on the guitar. This design is a sign-up bonus for fast responders to our CTA. We would like to see designs that incorporate our colors, if possible. The final design should be clean and simple.
Attached is a copy of my YouTube banner where you can get the colors from and my logo. I have also attached a clean looking example for you to refer to. Here is an additional resource provided as another example of how the final product should look: https://files.brindlecove.net/share/7KQX2mPLd9RaVt4Wn8ZcYe3Hs6BuJf-Q/view
The visuals will all need to be unified.

The main document is in Google Docs below. https://papers.brindlecove.net/doc/4TRmH8vKq2ZyLc7NbXa9WeP3Jd6GsUf5QoBn/edit?share=open
Updates

Here is an updated Google Docs link that is not restricted. https://papers.brindlecove.net/doc/4TRmH8vKq2ZyLc7NbXa9WeP3Jd6GsUf5QoBn/edit?share=open

Requirements
Nice to have
• SOCIAL MEDIA LINKS:

Instagram: https://www.snapgrove.net/strum.along.daily/
Facebook: https://www.friendvale.net/strumalongdaily
Twitter: https://chirpline.net/ned_harlow
YouTube: https://www.viewstream.net/channel/VXk3PqLm8RtZa2YwNc5HbEsd

```html
<!DOCTYPE html>
<html lang="en">
<head>
<meta charset="utf-8">
<title>Strum It Loud – Course Guide</title>
<link rel="stylesheet" href="https://fonts.googleapis.com/css2?family=Anton&family=Yellowtail&family=Montserrat:wght@500;600;700&family=Arimo:wght@400;700&family=Archivo+Black&display=swap">
<style>
:root{
  --backdrop:#a8a8a8;
  --red:#c83a30;
  --red-deep:#b2281f;
  --ink:#1b1b1b;
  --text:#3b3b3b;
  --paper:#f6f6f6;
  --stripe:#e9e9e9;
  --faint-pink:#f1d7d4;
}
*{margin:0;padding:0;box-sizing:border-box}
html,body{width:1200px;height:2613px;overflow:hidden}
body{background:var(--backdrop);position:relative;font-family:"Arimo",Arial,sans-serif;color:var(--text)}
.page{position:absolute;overflow:hidden;box-shadow:0 3px 10px rgba(0,0,0,.25)}

/* Cover */
.cover{left:326px;top:177px;width:564px;height:798px;background:linear-gradient(180deg,#cfcfcf 0%,#e2e2e2 35%,#f3e3dc 70%,#f7d3c8 100%)}
.cover-photo{position:absolute;left:80px;top:40px;width:400px;height:420px;border-radius:50% 50% 40% 40%;background:radial-gradient(ellipse at 50% 40%,#8f8f8f 0%,#b9b9b9 45%,rgba(220,220,220,0) 75%)}
.cover-glow{position:absolute;right:0;top:0;width:300px;height:160px;background:radial-gradient(ellipse at 80% 30%,rgba(232,125,50,.75),rgba(232,125,50,0) 70%)}
.cover-brand{position:absolute;left:0;right:0;top:400px;display:flex;justify-content:center;align-items:center;gap:10px;font-family:"Montserrat",sans-serif;font-weight:700;font-size:18px;color:var(--red-deep);letter-spacing:1px}
.dot{width:16px;height:16px;border-radius:50%;background:var(--red)}
.cover-title{position:absolute;left:0;right:0;top:478px;text-align:center;font-family:"Anton",sans-serif;font-weight:400;font-size:128px;line-height:1;color:var(--ink);letter-spacing:-2px}
.cover-script{position:absolute;left:0;right:0;top:565px;text-align:center;font-family:"Yellowtail",cursive;font-size:160px;line-height:1;color:var(--red);padding-left:30px}
.cover-tagline{position:absolute;left:0;right:0;top:733px;text-align:center;font-family:"Montserrat",sans-serif;font-weight:500;font-size:17px;color:var(--ink);letter-spacing:.5px}

/* Footer band shared */
.footer-band{position:absolute;left:0;right:0;bottom:0;height:56px;background:var(--red)}
.footer-side{position:absolute;bottom:56px;width:41px;height:38px;background:var(--red)}
.footer-side.left{left:0}.footer-side.right{right:0}
.footer-text{position:absolute;bottom:20px;font-family:"Arimo",sans-serif;font-weight:700;font-size:15px;color:#fff}

/* Contents */
.contents{left:51px;top:1054px;width:522px;height:736px;background:linear-gradient(180deg,#fff,var(--paper))}
.contents-label{position:absolute;left:58px;top:612px;transform:rotate(-90deg);transform-origin:0 0;font-family:"Archivo Black",sans-serif;font-size:47px;letter-spacing:2px;color:var(--faint-pink);white-space:nowrap}
.contents-frame{position:absolute;left:137px;top:56px;width:385px;height:550px;border-left:5px solid #ececec;border-top:5px solid #ececec;border-bottom:5px solid #ececec}
.contents-list{position:absolute;left:145px;top:77px;width:316px;list-style:none}
.contents-list li{display:flex;justify-content:space-between;height:23.6px;align-items:center;padding:0 17px 0 27px;font-size:11px;color:var(--text)}
.contents-list li:nth-child(odd){background:var(--stripe)}

/* Welcome */
.welcome{left:600px;top:1054px;width:522px;height:736px}
.welcome-photo{position:absolute;inset:0;background:linear-gradient(160deg,#6a5440 0%,#8f7456 30%,#b89c72 60%,#cdbf9c 100%)}
.welcome-tint{position:absolute;left:0;right:0;top:0;height:140px;background:linear-gradient(180deg,rgba(214,160,50,.7),rgba(214,160,50,.2))}
.welcome-title{position:absolute;left:105px;top:60px;font-family:"Archivo Black",sans-serif;font-size:62px;letter-spacing:1px;color:rgba(255,255,255,.45)}
.welcome-panel{position:absolute;left:222px;top:136px;width:300px;height:280px;background:rgba(250,244,236,.93);padding:18px 22px 0 10px;font-size:12px;line-height:1.25;color:var(--text)}
.welcome-panel h3{font-weight:700;font-size:13px;color:var(--red-deep);margin-bottom:6px}
.welcome-panel ul{list-style:none;margin:0 0 16px 8px}
.welcome-panel li{position:relative;padding-left:14px;margin-bottom:8px}
.welcome-panel li::before{content:"";position:absolute;left:0;top:4px;width:7px;height:7px;border-radius:50%;background:var(--red-deep)}
.welcome-panel p{margin:0 0 14px 8px}
.welcome-panel p.justify{text-align:justify}

/* Take your pick */
.pick{left:61px;top:1824px;width:522px;height:736px;background:var(--paper)}
.pick-header{position:absolute;left:0;top:0;width:522px;height:205px;background:#0c0c0c}
.pick-photo{position:absolute;left:0;top:0;width:170px;height:205px;background:radial-gradient(ellipse at 40% 50%,#c06a25 0%,#6b3510 45%,#0c0c0c 80%)}
.pick-title{position:absolute;left:110px;top:64px;font-family:"Archivo Black",sans-serif;font-size:33px;line-height:1;color:var(--red);letter-spacing:.5px;white-space:nowrap}
.pick-rule{position:absolute;left:446px;top:89px;width:76px;height:2px;background:var(--red)}
.pick-intro{position:absolute;left:106px;top:108px;width:370px;font-weight:700;font-size:9.6px;line-height:1.22;color:#fff;text-align:center}
.pick-body{position:absolute;left:40px;top:222px;width:433px;font-size:10px;line-height:1.4;color:var(--text)}
.pick-body h4{display:flex;align-items:center;gap:6px;font-weight:700;font-size:10.5px;color:var(--red-deep);margin-bottom:2px}
.pick-body h4::after{content:"";flex:1;height:1px;background:var(--red)}
.pick-body section{margin-bottom:26px}
.pick-body p{margin-bottom:12px}
.posture{position:absolute;left:42px;top:424px;width:438px;height:254px;border:3px solid #fff;background:#efefef}
.posture-sub{position:absolute;left:30px;top:236px;transform:rotate(-90deg);transform-origin:0 0;font-family:"Archivo Black",sans-serif;font-size:19px;color:var(--red);white-space:nowrap}
.posture-head{position:absolute;left:66px;top:236px;transform:rotate(-90deg);transform-origin:0 0;font-family:"Archivo Black",sans-serif;font-size:43px;line-height:1;color:var(--red);white-space:nowrap}
.posture-text{position:absolute;left:134px;top:20px;width:270px;font-size:10px;line-height:1.35}
.posture-photo{position:absolute;left:124px;top:100px;width:294px;height:120px;border-radius:60px 20px 20px 60px;background:linear-gradient(100deg,#e89a30 0%,#c77018 45%,#8c3a16 100%)}

/* Brand mark */
.brand-mark{position:absolute;left:700px;top:2188px;display:flex;align-items:center;gap:12px;font-family:"Montserrat",sans-serif;font-weight:700;font-size:26px;color:var(--red-deep)}
.brand-mark .dot{width:28px;height:28px}
</style>
</head>
<body>

<article class="page cover">
  <div class="cover-photo" role="img" aria-label="Guitar teacher playing an acoustic guitar against clouds"></div>
  <div class="cover-glow"></div>
  <div class="cover-brand"><span class="dot"></span>STRUM ALONG DAILY</div>
  <h1 class="cover-title">STRUM IT</h1>
  <div class="cover-script">Loud</div>
  <p class="cover-tagline">TO MASTER STRUMMING LIKE A ROCK STAR!</p>
</article>

<article class="page contents">
  <div class="contents-label">TABLE OF CONTENT</div>
  <div class="contents-frame"></div>
  <ol class="contents-list">
    <li><span>Welcome</span><span>03</span></li>
    <li><span>Take Your Pick</span><span>04</span></li>
    <li><span>Finger It Out - Using fingers instead of picks</span><span>05</span></li>
    <li><span>With or Without You</span><span>06</span></li>
    <li><span>Strike a Pose - Sit Up!</span><span>07</span></li>
    <li><span>We Got the Beat (Where’s the Beat?)</span><span>08</span></li>
    <li><span>Say What You Need to Say</span><span>09</span></li>
    <li><span>RELAX.</span><span>10</span></li>
    <li><span>Start Me Up!</span><span>11</span></li>
    <li><span>INSERT VIDEO LINK TO THIS IMAGE</span><span>12</span></li>
    <li><span>Adding the Up Strums</span><span>13</span></li>
    <li><span>Adding the Up Strums</span><span>14</span></li>
    <li><span>Paint the Fence, Kiddo</span><span>15</span></li>
    <li><span>Keep strumming hand always moving</span><span>16</span></li>
    <li><span>Don’t up strum every single string.</span><span>17</span></li>
    <li><span>Don’t Change Chords (yet).</span><span>18</span></li>
    <li><span>Reading Strums</span><span>19</span></li>
    <li><span>Back to One</span><span>20</span></li>
    <li><span>Mama, Don’t Take my (Metronome) Away</span><span>21</span></li>
    <li><span>Play With a Drummer</span><span>22</span></li>
    <li><span>Slow Ride (Take it Easy)</span><span>23</span></li>
    <li><span>Read Ahead</span><span>24</span></li>
  </ol>
  <div class="footer-side left"></div><div class="footer-side right"></div>
  <div class="footer-band"></div>
  <span class="footer-text" style="left:41px">WWW.WEBADDRESS.COM</span>
  <span class="footer-text" style="right:43px">01</span>
</article>

<article class="page welcome">
  <div class="welcome-photo" role="img" aria-label="Man holding an acoustic guitar while walking through tall grass"></div>
  <div class="welcome-tint"></div>
  <h2 class="welcome-title">WELCOME</h2>
  <div class="welcome-panel">
    <h3>What you will need one of the following</h3>
    <ul><li>A pick</li><li>Your thumb</li><li>The back of your fingernails</li></ul>
    <p>Can you count to four? Can you do it again? Then you can play rhythm!</p>
    <p>Okay, it’s not that easy. But it is that simple.</p>
    <p class="justify">Before we get started, I want to cover a few necessary things that will help along the way. These are several mistakes that folks do when just starting to learn how to strum effectively.</p>
  </div>
</article>

<article class="page pick">
  <div class="pick-header">
    <div class="pick-photo" role="img" aria-label="Acoustic guitar body in warm light"></div>
    <h2 class="pick-title">TAKE YOUR PICK</h2>
    <div class="pick-rule"></div>
    <p class="pick-intro">While you can play with your thumb and fingers, a pick will definitely give you an advantage. To hold a pick, use your thumb and index finger only. The pick should be facing the same way as your index finger, not your thumb. Hold pick closely to tip. Not like a dead mouse. This will help prevent dropping your pick into the soundhole (which stinks and should be avoided. It’s a rear pain in the neck retrieving them inside an acoustic guitar).</p>
  </div>
  <div class="pick-body">
    <section>
      <h4>FINGER IT OUT - USING FINGERS INSTEAD OF PICKS</h4>
      <p>Make like you are holding a pick. Use your index fingernail when you strum down, your thumbnail when you strum up, from the elbow</p>
    </section>
    <section>
      <h4>WITH OR WITHOUT YOU</h4>
      <p>People usually prefer one or the other, and will sometimes forsake the other. I had a student who would only use his thumb for any kind of strumming. Then he wanted to learn a very fast song (Skybreaker by Voltline) and he just couldn’t do it. He had six months of playing under his belt and had to start learning how to use a pick for the first time. It was awkward for him.</p>
      <p>My suggestion is to do both. In the beginning, you should learn and do both regularly. It’s like learning two languages at the same time.</p>
    </section>
  </div>
  <div class="footer-band" style="height:90px"></div>
  <div class="posture">
    <div class="posture-sub">STRIKE A POSE -</div>
    <div class="posture-head">SIT UP!</div>
    <p class="posture-text">Obviously, sitting up straight will help your strumming, but you’d be surprised how many folks try strumming while lying lazily on their couch or bed and wonder why they’re having problems.</p>
    <div class="posture-photo" role="img" aria-label="Classical acoustic guitar lying on its side"></div>
  </div>
  <span class="footer-text" style="left:40px">WWW.WEBADDRESS.COM</span>
  <span class="footer-text" style="right:43px">03</span>
</article>

<div class="brand-mark"><span class="dot"></span>STRUM ALONG DAILY</div>

</body>
</html>
```